Ridgeway Mortgage - Banner Ads for Re-Marketing Campaigns

Need a banner ad for a retargeting Campaign with Bright Tally.

We would like to incorporate our attached logo. Also would like to incorporate a call to action "Pre-Qualify for a home loan today" and a button to click. This banner is to encourage previous customers to come back to our website and submit information. It must look good on mobile and desktop.

Our website is RidgewayMortgage.com

Target Market(s)

Customers Seeking a Mortgage Loan

Industry/Entity Type

Mortgage

Requirements
Must have
• We would like the same basic design in the 4 sizes below.
• 728 pixels by 90 pixels leaderboard
• 300 by 250 medium rectangle
• 300 by 600 half page
• 320 by 100 mobile banner
Nice to have
• a Call to action, a button to click, animation
Should not have
• We are open.

```html
<!DOCTYPE html>
<html lang="en">
<head>
<meta charset="utf-8">
<title>Ridgeway Mortgage – Banner Set</title>
<link href="https://fonts.googleapis.com/css2?family=Quattrocento:wght@400&family=Open+Sans:wght@700&display=swap" rel="stylesheet">
<style>
  :root {
    --stage: #232323;
    --white: #ffffff;
    --ocean: #29a1e1;
    --navy: #1f5f8b;
    --brand-ink: #1a4f7a;
    --roof: #c8452a;
    --walls: #d8c3a0;
    --serif: "Quattrocento", Georgia, serif;
    --sans: "Open Sans", Arial, sans-serif;
  }
  * { margin: 0; padding: 0; box-sizing: border-box; }
  html, body { width: 1200px; height: 1200px; overflow: hidden; background: var(--stage); }
  .stage { position: relative; width: 1200px; height: 1200px; }

  .banner { position: absolute; background: var(--white); overflow: hidden; }
  .banner__wave { position: absolute; inset: 0; width: 100%; height: 100%; }
  .banner__wave path { fill: var(--ocean); }

  .brand { position: absolute; display: flex; align-items: center; gap: 10px;
    font-family: var(--serif); color: var(--brand-ink); text-transform: uppercase; line-height: 1.05; letter-spacing: .04em; }
  .brand__dot { flex: none; border-radius: 50%; background: var(--ocean); }

  .artwork { position: absolute; border-radius: 8px;
    background: linear-gradient(180deg, var(--roof) 0%, var(--roof) 42%, var(--walls) 43%, #c9b189 100%); }

  .headline { position: absolute; font-family: var(--serif); color: var(--white); font-weight: 400; }
  .cta { position: absolute; display: flex; align-items: center; justify-content: center;
    background: var(--navy); color: var(--white); font-family: var(--sans); font-weight: 700;
    text-transform: uppercase; border-radius: 3px; text-decoration: none; }

  /* 728 x 90 leaderboard */
  .leaderboard { left: 114px; top: 127px; width: 972px; height: 120px; }
  .leaderboard .brand { left: 26px; top: 30px; font-size: 27px; }
  .leaderboard .brand__dot { width: 50px; height: 50px; }
  .leaderboard .artwork { left: 462px; top: 20px; width: 105px; height: 92px; }
  .leaderboard .headline { left: 693px; top: 12px; font-size: 24px; line-height: 31px; }
  .leaderboard .cta { left: 837px; top: 65px; width: 111px; height: 42px; font-size: 13px; }

  /* 300 x 600 half page */
  .half-page { left: 139px; top: 301px; width: 358px; height: 715px; }
  .half-page .brand { left: 31px; top: 22px; font-size: 28px; }
  .half-page .brand__dot { width: 54px; height: 54px; }
  .half-page .artwork { left: 13px; top: 195px; width: 242px; height: 220px; }
  .half-page .headline { left: 25px; top: 495px; font-size: 40px; line-height: 48px; }
  .half-page .cta { left: 25px; top: 651px; width: 122px; height: 46px; font-size: 15px; }

  /* 300 x 250 medium rectangle */
  .medium-rectangle { left: 710px; top: 414px; width: 375px; height: 313px; }
  .medium-rectangle .brand { left: 15px; top: 52px; font-size: 14px; gap: 6px; }
  .medium-rectangle .brand__dot { width: 28px; height: 28px; }
  .medium-rectangle .artwork { left: 14px; top: 106px; width: 167px; height: 150px; }
  .medium-rectangle .headline { left: 231px; top: 168px; font-size: 24px; line-height: 29px; }
  .medium-rectangle .cta { left: 231px; top: 261px; width: 104px; height: 40px; font-size: 13px; }

  /* 320 x 100 mobile banner */
  .mobile-banner { left: 568px; top: 858px; width: 508px; height: 158px; }
  .mobile-banner .brand { left: 16px; top: 26px; font-size: 12px; gap: 6px; }
  .mobile-banner .brand__dot { width: 22px; height: 22px; }
  .mobile-banner .artwork { left: 116px; top: 45px; width: 120px; height: 105px; }
  .mobile-banner .headline { left: 370px; top: 16px; font-size: 21px; line-height: 27px; }
  .mobile-banner .cta { left: 370px; top: 104px; width: 108px; height: 40px; font-size: 12px; }
</style>
</head>
<body>
<main class="stage">

  <section class="banner leaderboard" aria-label="Leaderboard banner">
    <svg class="banner__wave" viewBox="0 0 972 120" preserveAspectRatio="none" aria-hidden="true">
      <path d="M542,20 C610,20 640,60 645,80 L688,0 H972 V120 H590 C615,90 612,40 542,20 Z"/>
    </svg>
    <div class="brand"><span class="brand__dot"></span><span>Ridgeway<br>Mortgage</span></div>
    <div class="artwork" role="img" aria-label="3D house built from the words Real Estate with a red roof"></div>
    <h2 class="headline">Pre-Qualify<br>for a home<br>loan today</h2>
    <a class="cta" href="#">Click here</a>
  </section>

  <section class="banner half-page" aria-label="Half page banner">
    <svg class="banner__wave" viewBox="0 0 358 715" preserveAspectRatio="none" aria-hidden="true">
      <path d="M57,138 C200,110 320,190 358,290 V715 H0 V445 C100,510 270,470 281,330 C292,230 200,140 57,138 Z"/>
    </svg>
    <div class="brand"><span class="brand__dot"></span><span>Ridgeway<br>Mortgage</span></div>
    <div class="artwork" role="img" aria-label="3D house built from the words Real Estate with a red roof"></div>
    <h2 class="headline">Pre-Qualify<br>for a home<br>loan today</h2>
    <a class="cta" href="#">Click here</a>
  </section>

  <section class="banner medium-rectangle" aria-label="Medium rectangle banner">
    <svg class="banner__wave" viewBox="0 0 375 313" preserveAspectRatio="none" aria-hidden="true">
      <path d="M46,25 C150,0 260,80 290,162 L346,0 H375 V313 H0 V262 C120,300 220,230 218,146 C215,70 140,20 46,25 Z"/>
    </svg>
    <div class="brand"><span class="brand__dot"></span><span>Ridgeway<br>Mortgage</span></div>
    <div class="artwork" role="img" aria-label="3D house built from the words Real Estate with a red roof"></div>
    <h2 class="headline">Pre-Qualify<br>for a home<br>loan today</h2>
    <a class="cta" href="#">Click here</a>
  </section>

  <section class="banner mobile-banner" aria-label="Mobile banner">
    <svg class="banner__wave" viewBox="0 0 508 158" preserveAspectRatio="none" aria-hidden="true">
      <path d="M156,22 C230,5 300,70 316,118 L360,0 H508 V158 H256 C278,130 276,70 240,45 C210,25 180,20 156,22 Z"/>
    </svg>
    <div class="brand"><span class="brand__dot"></span><span>Ridgeway<br>Mortgage</span></div>
    <div class="artwork" role="img" aria-label="3D house built from the words Real Estate with a red roof"></div>
    <h2 class="headline">Pre-Qualify<br>for a home<br>loan today</h2>
    <a class="cta" href="#">Click here</a>
  </section>

</main>
</body>
</html>
```